Amber Kettle Corp Business Card Design

Amber Kettle Corp is a local owner and operator of several coffee shops in Irving, TX. Google "Bean Harbor Plaza" for an example of one of our shops.We would like an image that is professional, but with a slight nod to the protestant religious nature of our backers.The name "Amber Kettle" is a play on the concept of "rivers of living water". It also conveys the concept of a "life of coffee". We desire to combine these concepts in the logo visualization, with the emphasis on the commercial side of the concept.

Target Market(s)

Upper class retail. No drive-through. Comfy lounges.

Industry/Entity Type

Coffee Shop

Contact Information for Business Card

Dale Fenwick
Chief Operating Officer
Amber Kettle Corp
(555) 417 2906
dale@amberkettle.example (address not yet active)

Requirements
Must have
• We do not have a logo yet. Need that as a part of the design.
• This needs to be original artwork. I need to own the art when the design is finished. I will look at submissions with stock artwork, but be advised that I will not accept the submission until original work is presented.

```html
<!DOCTYPE html>
<html lang="en">
<head>
<meta charset="utf-8">
<title>Amber Kettle Corp – Business Card</title>
<link rel="stylesheet" href="https://fonts.googleapis.com/css2?family=Titan+One&family=Lato:wght@400;700;900&display=swap">
<style>
  :root {
    --page: #ffffff;
    --brown: #4a3f36;
    --cream: #fdfbe6;
    --olive-deep: #55532f;
    --olive-dark: #66643a;
    --olive-mid: #8e8b4a;
    --olive-soft: #aaa75c;
    --olive-light: #d4d274;
  }
  html, body {
    margin: 0;
    padding: 0;
    width: 1200px;
    height: 1200px;
    overflow: hidden;
    background: var(--page);
  }
  .sheet {
    position: relative;
    width: 1200px;
    height: 1200px;
  }
  .card {
    position: absolute;
    width: 540px;
    height: 900px;
    overflow: hidden;
  }
  .card--front { left: 38px; top: 160px; }
  .card--back  { left: 619px; top: 158px; }

  .card__bands {
    position: absolute;
    inset: 0;
    width: 540px;
    height: 900px;
  }
  .card__swirl {
    position: absolute;
    inset: 0;
    background:
      radial-gradient(circle at 50% 50%, rgba(160,157,86,0.55) 0%, rgba(160,157,86,0) 55%),
      linear-gradient(160deg, var(--olive-deep) 0%, var(--olive-mid) 45%, var(--olive-dark) 100%);
  }

  .brand-name {
    position: absolute;
    left: 0;
    width: 540px;
    margin: 0;
    text-align: center;
    font-family: "Titan One", sans-serif;
    font-weight: 400;
    color: var(--cream);
    font-size: 52px;
    line-height: 1.05;
  }
  .card--front .brand-name { top: 205px; }
  .card--back  .brand-name { top: 390px; }

  .person {
    position: absolute;
    left: 0;
    top: 525px;
    width: 540px;
    text-align: center;
    font-family: "Titan One", sans-serif;
  }
  .person__name {
    margin: 0;
    font-size: 40px;
    line-height: 1;
    letter-spacing: 1px;
    text-transform: uppercase;
    color: var(--brown);
  }
  .person__name-last { color: var(--cream); }
  .person__title {
    margin: 6px 0 0;
    font-size: 20px;
    letter-spacing: 1px;
    text-transform: uppercase;
    color: var(--brown);
  }

  .phone {
    position: absolute;
    left: 85px;
    top: 694px;
    width: 369px;
    height: 66px;
    border-radius: 10px;
    background: var(--brown);
    color: var(--cream);
    font-family: "Lato", sans-serif;
    font-weight: 900;
    font-size: 36px;
    line-height: 66px;
    text-align: center;
    letter-spacing: 0.5px;
  }
  .email {
    position: absolute;
    left: 0;
    top: 772px;
    width: 540px;
    text-align: center;
    font-family: "Lato", sans-serif;
    font-size: 21px;
    color: var(--brown);
  }
</style>
</head>
<body>
<main class="sheet">

  <section class="card card--front" aria-label="Card front">
    <svg class="card__bands" viewBox="0 0 540 900" aria-hidden="true">
      <rect width="540" height="900" fill="var(--olive-light)"/>
      <polygon points="0,380 540,700 540,900 0,900" fill="var(--olive-soft)" opacity="0.35"/>
      <polygon points="0,0 540,0 540,700 0,380" fill="var(--olive-mid)"/>
      <polygon points="0,200 540,500 540,680 0,380" fill="var(--olive-dark)"/>
      <polygon points="0,0 540,0 540,340 0,20" fill="var(--olive-deep)"/>
    </svg>

    <p class="brand-name">Amber Kettle<br>Corp</p>

    <div class="person">
      <h1 class="person__name">Dale <span class="person__name-last">Fenwick</span></h1>
      <p class="person__title">Chief Operating Officer</p>
    </div>

    <div class="phone">(555) 417 2906</div>
    <div class="email">dale@amberkettle.example</div>
  </section>

  <section class="card card--back" aria-label="Card back">
    <div class="card__swirl" role="img" aria-label="Olive green swirling sunburst background pattern"></div>
    <p class="brand-name">Amber Kettle<br>Corp</p>
  </section>

</main>
</body>
</html>
```